Brava Set CEO and Partners Business Card

We need a fresh, fun, simple and clean business card design....we would like a template where we can add a name and title (as well as specific email addresses). We are open to different looks (full logo on one side and a small logo on the company info side, or our logo is in the background but faint on one side but full on the other, or something else cool :-) ). Our colors are in our logo: blue, black and white...however we are not opposed to the use of other colors if it works. We build sets, make props and a host of other things for the film and television industry...our card should reflect creativity, style and professionalism.

A white background would be preferred.

I would like to see an option with Facebook and Instagram icons.

Facebook- facebook.com/bravasetny
Instagram- brava_set

Our website is bravaset-example.com.

Brava Set, Inc.
418 Corvell Avenue, Unit 9
Ridgeview Park, Nevada 89170
555.210.4873 | tel
555.210.6692 | fax
www.BravaSet-example.com

Sample Name and Title #1:

Peter Halvik
CEO / Co-Owner
555.210.4873 | tel
555.210.6692 | fax
peter@bravaset-example.com
www.BravaSet-example.com

Target Market(s)

Marketing Professionals, Production Designers, Interior Designers, Film Producers, Directors, Art Directors, Event Directors

Industry/Entity Type

Entertainment Industry

Contact Information for Business Card

Peter Halvik
CEO / Co-Owner
555.210.4873 | tel
555.210.6692 | fax
peter@bravaset-example.com
www.BravaSet-example.com

Font styles to use
Sans Serif

Colors
33a6d7
ffffff
1b1b1b

Requirements
Must have
• Logo, All Contact Info, White Background. Symmetry.
Nice to have
• Facebook and Instagram icons with addresses
• Facebook- facebook.com/bravasetny
• Instagram- brava_set

```html
<!DOCTYPE html>
<html lang="en">
<head>
<meta charset="utf-8">
<title>Brava Set — Business Card</title>
<link rel="stylesheet" href="https://fonts.googleapis.com/css2?family=Roboto:wght@400;500;700&display=swap">
<style>
  :root {
    --brand-blue: #33a6d7;
    --brand-black: #1b1b1b;
    --brand-white: #ffffff;
    --stage: #e9e7e4;
    --ink: #1b1b1b;
  }
  * { box-sizing: border-box; margin: 0; padding: 0; }
  html, body {
    width: 1200px; height: 900px; overflow: hidden;
    background: var(--stage);
    font-family: "Roboto", Arial, sans-serif;
  }
  .canvas { position: relative; width: 1200px; height: 900px; }

  .card {
    position: absolute; top: 300px;
    width: 525px; height: 300px;
    overflow: hidden;
    box-shadow: 0 6px 18px rgba(0,0,0,0.18);
  }

  /* Front */
  .card--front { left: 50px; background: var(--brand-black); }
  .front-logo {
    position: absolute; inset: 0;
    display: flex; align-items: center; justify-content: center;
    color: var(--brand-white);
    font-weight: 700; font-size: 54px; letter-spacing: 1px;
  }

  /* Back */
  .card--back { left: 625px; background: var(--brand-white); color: var(--ink); }
  .holder { position: absolute; left: 30px; top: 30px; }
  .holder-name { font-size: 19px; font-weight: 700; color: var(--brand-black); }
  .holder-title { font-size: 11px; font-weight: 400; color: var(--brand-blue); margin-top: 2px; }

  .back-logo {
    position: absolute; right: 30px; top: 92px;
    font-size: 42px; font-weight: 700; color: var(--brand-black); letter-spacing: 1px;
  }

  .contact-list { position: absolute; left: 30px; top: 150px; list-style: none; }
  .contact-item {
    display: flex; align-items: center; gap: 7px;
    font-size: 12.5px; line-height: 17px; color: var(--ink);
  }
  .contact-icon { width: 12px; height: 12px; flex: none; }

  .address {
    position: absolute; right: 30px; top: 212px;
    font-size: 13px; line-height: 17px; color: var(--ink);
    font-style: normal; text-align: left;
  }

  .footer-band { position: absolute; left: 0; bottom: 0; width: 525px; height: 44px; }
  .social-list {
    position: absolute; right: 26px; bottom: 9px;
    display: flex; gap: 22px; list-style: none;
  }
  .social-item {
    display: flex; align-items: center; gap: 6px;
    color: var(--brand-white); font-size: 12.5px;
  }
  .social-mark { width: 10px; height: 10px; background: var(--brand-blue); flex: none; }
</style>
</head>
<body>
<main class="canvas">

  <section class="card card--front" aria-label="Card front">
    <div class="front-logo">BRAVA SET</div>
  </section>

  <section class="card card--back" aria-label="Card back">
    <div class="holder">
      <p class="holder-name">Peter Halvik</p>
      <p class="holder-title">CEO / Co-Owner</p>
    </div>

    <div class="back-logo">BRAVA SET</div>

    <ul class="contact-list">
      <li class="contact-item">
        <svg class="contact-icon" viewBox="0 0 12 12" aria-hidden="true"><path fill="#33a6d7" d="M2.5 1h2l1 2.6-1.3 1a6 6 0 0 0 3.2 3.2l1-1.3L11 7.5v2c0 .8-.7 1.5-1.5 1.5A8.5 8.5 0 0 1 1 2.5C1 1.7 1.7 1 2.5 1z"/></svg>
        555.210.4873
      </li>
      <li class="contact-item">
        <svg class="contact-icon" viewBox="0 0 12 12" aria-hidden="true"><rect x="3" y="1" width="6" height="3" fill="#33a6d7"/><rect x="1" y="4.5" width="10" height="5" rx="1" fill="#33a6d7"/><rect x="3" y="8" width="6" height="3" fill="#fff" stroke="#33a6d7"/></svg>
        555.210.6692
      </li>
      <li class="contact-item">
        <svg class="contact-icon" viewBox="0 0 12 12" aria-hidden="true"><rect x="1" y="2.5" width="10" height="7" fill="#33a6d7"/><path d="M1.5 3l4.5 3.5L10.5 3" fill="none" stroke="#fff" stroke-width="1"/></svg>
        peter@bravaset-example.com
      </li>
      <li class="contact-item">
        <svg class="contact-icon" viewBox="0 0 12 12" aria-hidden="true"><circle cx="6" cy="6" r="5" fill="none" stroke="#33a6d7" stroke-width="1.2"/><ellipse cx="6" cy="6" rx="2" ry="5" fill="none" stroke="#33a6d7"/><path d="M1 6h10" stroke="#33a6d7"/></svg>
        www.BravaSet-example.com
      </li>
    </ul>

    <address class="address">
      418 Corvell Avenue, Unit 9<br>
      Ridgeview Park, Nevada 89170
    </address>

    <svg class="footer-band" viewBox="0 0 525 44" aria-hidden="true">
      <polygon points="0,34 285,34 300,14 525,14 525,44 0,44" fill="#1b1b1b"/>
    </svg>
    <ul class="social-list">
      <li class="social-item"><span class="social-mark"></span>bravasetny</li>
      <li class="social-item"><span class="social-mark"></span>brava_set</li>
    </ul>
  </section>

</main>
</body>
</html>
```